VL6 (acronym stands for Vendlane 6)

We are a sales and marketing start up. We sell bar and beverage dispensing equipment presently and we will add foodservice equipment to our portfolio in the coming year. We like our logo but we will consider different presentations of "VL6"

Industry/Entity Type

Marketing

```html
<!DOCTYPE html>
<html lang="en">
<head>
<meta charset="utf-8">
<title>VL6 Business Cards</title>
<link href="https://fonts.googleapis.com/css2?family=Lato:wght@400;700;900&display=swap" rel="stylesheet">
<style>
  :root {
    --page-bg: #e9e6e1;
    --card-light: #f7f7f7;
    --card-light-edge: #dcdcdc;
    --card-dark: #111111;
    --ink-dark: #1a1a1a;
    --ink-muted: #6a6a6a;
    --ink-light: #f2f2f2;
    --ink-light-muted: #b5b5b5;
    --rule-light: #9a9a9a;
    --rule-dark: #6d6d6d;
  }
  * { box-sizing: border-box; margin: 0; padding: 0; }
  html, body {
    width: 1200px;
    height: 1023px;
    overflow: hidden;
    background: var(--page-bg);
    font-family: "Lato", Arial, sans-serif;
  }
  .sheet {
    position: relative;
    width: 1200px;
    height: 1023px;
  }
  .card {
    position: absolute;
    width: 540px;
    height: 309px;
    border-radius: 22px;
    display: flex;
    align-items: center;
    padding: 0 34px;
  }
  .card--light {
    left: 40px;
    top: 200px;
    background: linear-gradient(135deg, #ffffff 0%, var(--card-light) 55%, #ececec 100%);
    border: 1px solid var(--card-light-edge);
    box-shadow: 0 6px 18px rgba(0,0,0,0.12);
    color: var(--ink-dark);
  }
  .card--dark {
    left: 620px;
    top: 514px;
    background: linear-gradient(135deg, #2a2a2a 0%, var(--card-dark) 45%, #000000 100%);
    box-shadow: 0 6px 18px rgba(0,0,0,0.25);
    color: var(--ink-light);
  }
  .brand {
    width: 240px;
    display: flex;
    align-items: center;
    justify-content: center;
    gap: 12px;
  }
  .brand__mark {
    width: 16px;
    height: 16px;
    background: currentColor;
  }
  .brand__name {
    font-weight: 900;
    font-size: 86px;
    letter-spacing: -2px;
    line-height: 1;
  }
  .divider {
    width: 1px;
    height: 190px;
    margin: 0 22px 0 14px;
  }
  .card--light .divider { background: linear-gradient(to bottom, transparent, var(--rule-light), transparent); }
  .card--dark .divider { background: linear-gradient(to bottom, transparent, var(--rule-dark), transparent); }
  .contact__name {
    font-weight: 700;
    font-size: 22px;
    line-height: 1.1;
  }
  .contact__role {
    font-size: 15px;
    margin-bottom: 10px;
  }
  .card--light .contact__role { color: var(--ink-muted); }
  .card--dark .contact__role { color: var(--ink-light-muted); }
  .contact__list { list-style: none; }
  .contact__item {
    display: flex;
    align-items: center;
    gap: 7px;
    font-size: 16px;
    line-height: 1.5;
  }
  .contact__icon { width: 13px; height: 13px; flex: none; }
</style>
</head>
<body>
<main class="sheet">

  <section class="card card--light" aria-label="Business card, light version">
    <div class="brand">
      <span class="brand__mark"></span>
      <span class="brand__name">VL6</span>
    </div>
    <div class="divider"></div>
    <div class="contact">
      <p class="contact__name">Dana Morrow</p>
      <p class="contact__role">Owner</p>
      <ul class="contact__list">
        <li class="contact__item">
          <svg class="contact__icon" viewBox="0 0 16 16"><path fill="currentColor" d="M3 1h3l1.5 4-2 1.3a9 9 0 0 0 4.2 4.2L11 8.5l4 1.5v3a2 2 0 0 1-2 2A12 12 0 0 1 1 3a2 2 0 0 1 2-2z"/></svg>
          1-555-014-2290
        </li>
        <li class="contact__item">
          <svg class="contact__icon" viewBox="0 0 16 16"><rect x="1" y="3" width="14" height="10" fill="currentColor"/><path d="M1 3l7 6 7-6" stroke="#fff" stroke-width="1.4" fill="none"/></svg>
          info@VL6.ca
        </li>
        <li class="contact__item">
          <svg class="contact__icon" viewBox="0 0 16 16"><rect x="1.5" y="2" width="13" height="9" fill="none" stroke="currentColor" stroke-width="1.5"/><path d="M5 14h6M8 11v3" stroke="currentColor" stroke-width="1.5"/></svg>
          www.vl6.ca
        </li>
      </ul>
    </div>
  </section>

  <section class="card card--dark" aria-label="Business card, dark version">
    <div class="brand">
      <span class="brand__mark"></span>
      <span class="brand__name">VL6</span>
    </div>
    <div class="divider"></div>
    <div class="contact">
      <p class="contact__name">Dana Morrow</p>
      <p class="contact__role">Owner</p>
      <ul class="contact__list">
        <li class="contact__item">
          <svg class="contact__icon" viewBox="0 0 16 16"><path fill="currentColor" d="M3 1h3l1.5 4-2 1.3a9 9 0 0 0 4.2 4.2L11 8.5l4 1.5v3a2 2 0 0 1-2 2A12 12 0 0 1 1 3a2 2 0 0 1 2-2z"/></svg>
          1-555-014-2290
        </li>
        <li class="contact__item">
          <svg class="contact__icon" viewBox="0 0 16 16"><rect x="1" y="3" width="14" height="10" fill="currentColor"/><path d="M1 3l7 6 7-6" stroke="#111" stroke-width="1.4" fill="none"/></svg>
          info@VL6.ca
        </li>
        <li class="contact__item">
          <svg class="contact__icon" viewBox="0 0 16 16"><rect x="1.5" y="2" width="13" height="9" fill="none" stroke="currentColor" stroke-width="1.5"/><path d="M5 14h6M8 11v3" stroke="currentColor" stroke-width="1.5"/></svg>
          www.vl6.ca
        </li>
      </ul>
    </div>
  </section>

</main>
</body>
</html>
```